Velimo Ventures Logo and Business Card Design

We already have the rough logo shape (however please make the lines on the logo much thicker so a dark background is not required to see it) . see photos uploaded.
It needs to be refined with color and digitized and then have a front and back business card layout done.
The services are high vibration healing support through a therapy and feng shui service offering. We want people to Feel Happiness, Feel Prosperity and Feel Peace. (the back of the card would have these phrases on it) So a warm, calm and peaceful feeling card.
We would like the card to use the logo provided (with thicker lines and color added) but below the graphic please use the name "Velimo Ventures" NOT Velimo.
We also would like to use the colors in the colorized matrix shown in photos (gold and purple) but on the lighter side. Thanks for your time!

Front of Card should include: Logo, with Company Name: Velimo Ventures as part of logo, Name: Mara Donne email: mara@velimo.example web: www.velimo.example mobile: 555.018.2946 at bottom of front list Family Constellation | Feng Shui

Back of Card should have the logo and the following listed vertically:

PERSONAL | BUSINESS (Larger size then smaller bullet items below)
*Find Happiness
*Find Prosperity
*Find Peace

Target Market(s)

Target market is both business and personal

Contact Information for Business Card

Front of Card should include: Logo, with Company Name: Velimo Ventures as part of logo, Name: Mara Donne email: mara@velimo.example web: www.velimo.example mobile: 555.018.2946 at bottom of front list Family Constellation | Feng Shui ++++ Back of Card should have the logo and the following listed vertically: PERSONAL | BUSINESS (Larger size then smaller bullet items below) *Find Happiness *Find Prosperity *Find Peace

Font styles to use
Sans Serif

Colors

Designer to choose colors to be used in the design.

Requirements
Nice to have
• Nice light contrast color for the back of card background
Should not have
• No dark colored background on Card.

```html
<!DOCTYPE html>
<html lang="en">
<head>
<meta charset="utf-8">
<title>Velimo Ventures – Business Cards</title>
<link rel="stylesheet" href="https://fonts.googleapis.com/css2?family=Montserrat:wght@400;500;600;700&display=swap">
<style>
  :root {
    --gold: #e2b42a;
    --gold-deep: #c99a1c;
    --gold-text: #d4a21f;
    --purple: #6a4fa8;
    --ink: #2b2418;
    --card: #ffffff;
    --backdrop: #ece9e4;
  }
  * { box-sizing: border-box; margin: 0; padding: 0; }
  html, body {
    width: 1200px; height: 786px; overflow: hidden;
    background: var(--backdrop);
    font-family: "Montserrat", sans-serif;
  }
  .stage {
    position: relative; width: 1200px; height: 786px;
  }
  .card {
    position: absolute;
    width: 540px; height: 310px;
    background: var(--card);
    overflow: hidden;
    box-shadow: 0 10px 28px rgba(40, 30, 20, .18);
  }
  .card--front { left: 40px; top: 238px; }
  .card--back  { left: 620px; top: 238px; }

  /* logo lockup */
  .brand {
    position: absolute;
    display: flex; align-items: center; gap: 10px;
  }
  .brand__mark {
    width: 34px; height: 34px; border-radius: 50%;
    border: 4px solid var(--purple);
  }
  .brand__name {
    color: var(--gold-text);
    font-weight: 600;
    letter-spacing: .06em;
    text-transform: uppercase;
  }
  .card--front .brand { right: 34px; top: 58px; }
  .card--front .brand__name { font-size: 22px; }
  .card--back .brand { left: 50%; top: 70px; transform: translateX(-50%); }
  .card--back .brand__name { font-size: 26px; }

  /* front */
  .divider {
    position: absolute; left: 150px; right: 20px; top: 176px;
    height: 1px; background: var(--gold);
  }
  .person {
    position: absolute; left: 30px; top: 188px;
  }
  .person__name {
    color: var(--gold-text); font-weight: 700;
    font-size: 20px; letter-spacing: .04em; text-transform: uppercase;
    margin-bottom: 8px;
  }
  .contact { list-style: none; }
  .contact li {
    display: flex; align-items: center; gap: 10px;
    font-size: 13px; color: var(--ink); line-height: 19px;
  }
  .contact svg { width: 12px; height: 12px; fill: var(--gold); flex: none; }
  .front-base {
    position: absolute; left: 0; bottom: 0; width: 540px; height: 70px;
  }
  .services {
    position: absolute; right: 22px; bottom: 22px;
    font-size: 13px; font-weight: 500; color: var(--ink);
  }

  /* back */
  .band {
    position: absolute; left: 0; right: 0; top: 178px; height: 46px;
    background: var(--gold);
    display: flex; align-items: center; justify-content: center;
  }
  .band__title {
    font-weight: 700; font-size: 16px; letter-spacing: .03em;
    color: var(--ink); text-transform: uppercase;
  }
  .offers {
    position: absolute; left: 0; right: 0; top: 236px;
    display: flex; justify-content: center; gap: 10px;
    list-style: none; font-size: 13px; color: var(--ink);
  }
  .offers li + li::before {
    content: "•"; color: var(--gold-deep); margin-right: 10px;
  }
  .back-edge {
    position: absolute; left: 0; right: 0; bottom: 0; height: 14px;
    background: var(--gold);
  }
</style>
</head>
<body>
<main class="stage">

  <section class="card card--front" aria-label="Front of business card">
    <div class="brand">
      <span class="brand__mark"></span>
      <span class="brand__name">Velimo Ventures</span>
    </div>

    <div class="divider"></div>

    <div class="person">
      <h1 class="person__name">Mara Donne</h1>
      <ul class="contact">
        <li>
          <svg viewBox="0 0 12 12" aria-hidden="true"><path d="M1 4c0-1.5 2.2-2.5 5-2.5S11 2.5 11 4v1H8.5V4h-5v1H1zM2.5 6h7l1 4.5h-9z"/></svg>
          555.018.2946
        </li>
        <li>
          <svg viewBox="0 0 12 12" aria-hidden="true"><path d="M0.5 2.5h11v7h-11z M1.5 3.2 6 6.6l4.5-3.4" stroke="#fff" stroke-width=".9"/></svg>
          mara@velimo.example
        </li>
        <li>
          <svg viewBox="0 0 12 12" aria-hidden="true"><circle cx="6" cy="6" r="5.5"/><path d="M1 6h10M6 .5c2 2 2 9 0 11M6 .5c-2 2-2 9 0 11" stroke="#fff" stroke-width=".8" fill="none"/></svg>
          www.velimo.example
        </li>
      </ul>
    </div>

    <svg class="front-base" viewBox="0 0 540 70" aria-hidden="true">
      <path d="M0 52 H300 L292 60 H0 Z" fill="var(--purple)"/>
      <path d="M0 62 H540 V70 H0 Z" fill="var(--gold)"/>
      <path d="M322 10 Q312 10 306 22 L290 62 H540 V10 Z" fill="var(--gold)"/>
    </svg>
    <p class="services">Family Constellation | Feng Shui</p>
  </section>

  <section class="card card--back" aria-label="Back of business card">
    <div class="brand">
      <span class="brand__mark"></span>
      <span class="brand__name">Velimo Ventures</span>
    </div>

    <div class="band">
      <h2 class="band__title">Business | Personal</h2>
    </div>
    <ul class="offers">
      <li>Find Happiness</li>
      <li>Find Prosperity</li>
      <li>Find Peace</li>
    </ul>
    <div class="back-edge"></div>
  </section>

</main>
</body>
</html>
```